Graphic background for 10 Pull Up Banners

To produce a graphic background for a 100 cm wide by 200 cm high Pull-Up Display banner containing a Buddhist text in three languages: Tibetan, Mandarin and English. Please refer to uploaded file "Elements of Pull Up Banner". The design should be simple (not drawing attention away from the text). This design should then be varied for or extended to the next banner and so on until the 10th banner. When the banners are lined up, they should form a single design that is 1000 cm wide by 200 cm high.
An alternative way to look at the project is to produce a graphic background of 1000 cm width by 200 cm height that is then splitted into ten separate 100 cm wide by 200 cm high graphic to be used as background for 10 Buddhist texts (text 1, 2, 3, 4, 5, 6, 7, 8, 9a, 9b) on 10 Pull-Up Display Banners, the text in each banner being in the three languages mentioned earlier.
In either perspective, the design should be simple and not draw attention away from the texts. See uploaded PDF file "Examples.pdf"
For attendees at a Buddhist Event.

```html
<!DOCTYPE html>
<html lang="en">
<head>
<meta charset="utf-8">
<title>Pull-Up Banner Series</title>
<link href="https://fonts.googleapis.com/css2?family=Noto+Sans:wght@400;700&family=Noto+Serif+SC:wght@400;600&family=Noto+Serif+Tibetan:wght@400&display=swap" rel="stylesheet">
<style>
  :root{
    --stage:#0d0f12;
    --paper:#ffffff;
    --paper-shade:#eef0f3;
    --title-blue:#2aa6e0;
    --title-orange:#f0a020;
    --ink:#1c2a8e;
    --ink-soft:#3a4a9a;
    --band-dark:#1466a8;
    --band-mid:#1d7fc4;
    --band-light:#9fd3f0;
  }
  *{box-sizing:border-box;margin:0;padding:0}
  html,body{width:1200px;height:1200px;overflow:hidden;background:var(--stage)}
  .series{
    width:1200px;height:1200px;
    display:grid;grid-template-columns:repeat(5,204px);grid-template-rows:repeat(2,408px);
    gap:44px 24px;justify-content:center;align-content:center;
  }
  .banner{
    position:relative;overflow:hidden;
    background:radial-gradient(circle at 70% 38%,var(--paper-shade) 0,var(--paper) 38%,var(--paper-shade) 62%,var(--paper) 80%);
    font-family:"Noto Sans",sans-serif;color:var(--ink);
    padding:14px 12px 0 12px;
  }
  .banner__header{margin-bottom:8px}
  .banner__title-zh{font-family:"Noto Serif SC",serif;color:var(--title-blue);font-size:8px;line-height:1.2}
  .banner__title-en{color:var(--title-orange);font-weight:700;font-size:6px;line-height:1.3}
  .text-bo{font-family:"Noto Serif Tibetan",serif;font-size:6.2px;line-height:1.55;margin:0 0 8px 8px}
  .text-zh{font-family:"Noto Serif SC",serif;font-size:5.6px;line-height:1.7;margin:0 0 6px 22px;color:var(--ink-soft)}
  .text-zh.wide{line-height:2.3;margin-left:30px}
  .notes{font-size:3.6px;color:var(--ink-soft);margin:0 0 8px 30px;line-height:1.6}
  .text-en{font-size:4.4px;line-height:1.45;font-weight:700}
  .text-en p{margin-bottom:3px}
  .text-en.regular{font-weight:400}
  .two-col{display:grid;grid-template-columns:1fr 1fr;gap:6px}
  .illustration{
    position:absolute;right:0;top:30px;width:92px;height:240px;
    background:linear-gradient(180deg,#f3f4f6,#e4e7ec);opacity:.8;
  }
  .illustration.left{left:0;right:auto;top:20px;width:110px;height:190px}
  .banner__content{position:relative}
  .base-band{
    position:absolute;left:0;right:0;bottom:0;height:68px;
    background:linear-gradient(135deg,var(--band-dark),var(--band-mid) 45%,var(--band-dark) 70%,var(--band-mid));
  }
  .base-band::before{
    content:"";position:absolute;left:0;right:0;top:-8px;height:8px;
    background:linear-gradient(180deg,var(--band-light),#cde9f8);
  }
  .emblem{
    position:absolute;right:12px;bottom:14px;width:32px;height:32px;border-radius:50%;
    background:rgba(255,255,255,.55);
  }
</style>
</head>
<body>
<main class="series">

  <article class="banner">
    <header class="banner__header"><div class="banner__title-zh">十个误解</div><div class="banner__title-en">Ten Mistaking</div></header>
    <div class="text-bo">དད་པ་དང་འདོད་ཆགས་འཁྲུལ་དུ་རུང་།<br>སྙིང་རྗེ་དང་ཞེན་པ་འཁྲུལ་དུ་རུང་།<br>སྟོང་པ་ཉིད་དང་བློ་བཟོ་འཁྲུལ་དུ་རུང་།<br>ཆོས་དབྱིངས་དང་ཆད་ལྟ་འཁྲུལ་དུ་རུང་།<br>ཉམས་དང་རྟོགས་པ་འཁྲུལ་དུ་རུང་།<br>ཆོས་པ་དང་གཡོ་ཅན་འཁྲུལ་དུ་རུང་།</div>
    <div class="text-zh">信心与爱欲可能混淆，<br>慈悲与贪执可能混淆，<br>所知本空与思维造作空性可能混淆，<br>法界与断见可能混淆，<br>觉受与证悟可能混淆，<br>尊者与神棍可能混淆，<br>破戒与著魔可能混淆，<br>成就者与骗子可能混淆，<br>利他与自利可能混淆，<br>方便善巧与伪装欺骗可能混淆。</div>
    <div class="notes">1. 所知：可以认识的事物。<br>2. 断见：否定因果、业报的见解。</div>
    <div class="text-en">
      Desire can be mistaken for faith or devotion.<br>Attachment can be mistaken for love and compassion.<br>Conceptual emptiness can be mistaken for the emptiness of the nature of phenomena.<br>Nihilism can be mistaken for the dharmadhatu.<br>A meditative experience can be mistaken for realization.<br>Outer religious practices can be mistaken for inner development of good qualities.<br>A person in the grip of a demon can be mistaken for a person who has destroyed his own delusions.<br>A charlatan can be mistaken for a siddha.<br>An act to benefit yourself can be mistaken for an act to benefit others.
    </div>
    <div class="base-band"><div class="emblem" role="img" aria-label="Lotus emblem"></div></div>
  </article>

  <article class="banner">
    <header class="banner__header"><div class="banner__title-zh">欲与爱</div><div class="banner__title-en">Desire &amp; Attachment</div></header>
    <div class="text-bo" style="margin-top:6px">འདོད་པ་མེད་ན་རང་དོན་མི་འགྲུབ་ཀྱང་།<br>འདོད་པ་ཡོད་ཚད་ཆགས་པ་མ་ཡིན་པས།<br>འདོད་དང་ཆགས་པའི་ཁྱད་པར་མ་ཕྱེད་པར།<br>འདོད་ཆགས་ལམ་དུ་བྱེད་ཟེར་བསྙོན་པར་ཟད།</div>
    <div class="text-zh wide">若无意欲则不成自利，<br>然有意欲非为执着故，<br>不知意欲执着差别即，<br>贪执说所当取确荒唐。</div>
    <div class="text-en" style="margin-top:60px">
      If you have no desire, your goal cannot be achieved.<br>Since not all desire is attachment,<br>not knowing how to differentiate desire from attachment,<br>to talk about bringing passion into the path is absurd.
    </div>
    <div class="base-band"><div class="emblem" role="img" aria-label="Butter lamp emblem"></div></div>
  </article>

  <article class="banner">
    <header class="banner__header"><div class="banner__title-zh">曾修过佛法的相状</div><div class="banner__title-en">Signs Of Having Practised The Dharma</div></header>
    <div class="text-bo">རང་ལུས་ལ་མ་ཞེན་པར་དལ་འབྱོར་གྱི་སྙིང་པོ་བླངས་ན།<br>གསེར་དང་རྡོ་ཁམ་མཉམ་པར་མཐོང་ན།<br>འཁོར་བའི་སྣང་བ་དགྲ་རུ་མཐོང་ན།<br>ཆོས་ཉམས་སུ་བླངས་པའི་རྟགས་ཡིན།</div>
    <div class="text-zh wide">若懂舍自身富而修行，<br>表示取得真贵暇满¹义；<br><br>若懂金与土块平等观，<br>表示'无常''如 幻'心中生；<br><br>若视轮回现象为敌人，<br>表示渡往苦海之彼岸。</div>
    <div class="notes">1. 暇满：八有暇和十圆满。</div>
    <div class="text-en regular">
      <p>If you know not to cherish your body but use it to attain accomplishments (in the Dharma), it is a sign that you have gotten the essence of your precious freedoms and fortunes¹.</p>
      <p>If you know the sameness of gold and dirt while in meditative equipoise, it is a sign that the insight of impermanence and illusion have arisen in your mental continuum.</p>
      <p>If you know to see samsaric phenomena as an enemy, it is a sign that you are heading to the other shore of the ocean of suffering.</p>
    </div>
    <div class="base-band"><div class="emblem" role="img" aria-label="Auspicious symbol emblem"></div></div>
  </article>

  <article class="banner">
    <header class="banner__header"><div class="banner__title-zh">上师之恩德</div><div class="banner__title-en">Kindness Of The Guru</div></header>
    <div class="text-bo" style="margin-left:24px">བླ་མའི་བཀའ་དྲིན་མ་བརྗེད་ཅིག།<br>སངས་རྒྱས་སྟོང་ཕྲག་བྱོན་ཡང་ནི།<br>ང་ལ་བསྐྱབས་པ་མ་བྱུང་ངོ་།<br>ཐུགས་རྗེས་ང་ལ་གཟིགས་པ་ཡི།<br>བཀའ་དྲིན་དེ་ལས་ཆེ་བ་མེད།</div>
    <div class="text-zh wide" style="margin-left:40px">切莫忘记上师，<br>即使众多佛降临，<br>谁皆未曾摄受我，<br>您不曾弃悲护我，<br>您比千佛恩更大。</div>
    <div class="text-en regular" style="margin-top:30px">
      <p>Do not forget the guru.</p>
      <p>Although many Buddhas had appeared, none has taken hold of me. You did not abandon me, but lovingly and compassionately protected me.</p>
      <p>Your kindness is greater than a thousand Buddhas.</p>
    </div>
    <div class="base-band"><div class="emblem" role="img" aria-label="Endless knot emblem"></div></div>
  </article>

  <article class="banner">
    <div class="illustration" role="img" aria-label="Faint line drawing of a seated deity"></div>
    <div class="banner__content">
      <header class="banner__header"><div class="banner__title-zh">您与佛法</div><div class="banner__title-en">You And The Dharma</div></header>
      <div class="text-bo" style="margin-left:0;width:120px">ཆོས་ཕུང་བརྒྱད་ཁྲི་བཞི་སྟོང་ནི།<br>རང་སེམས་བཏུལ་ཕྱིར་གསུངས་པ་ཡིན།<br>སེམས་ལ་ཕན་པར་མ་གྱུར་ན།<br>ཆོས་ཀྱིས་ཁྱོད་ལ་ཅི་ཕན་ཡོད།<br>ཆོས་དང་སེམས་ནི་འདྲེས་པར་གྱིས།</div>
      <div class="text-zh" style="margin-left:96px">八万四千法门佛本，<br>原为驯伏自心一者中，<br>若心未受法益，<br>法于你有何利益，<br>应令法与心相融，<br>方是修法之精要。</div>
      <div class="text-en regular" style="margin-top:14px">
        <p>The eighty-four thousand Dharma doors are solely for subduing your own mind.</p>
        <p>If your mind is not tamed despite hearing many teachings, what benefit will the Dharma bring you at the time of death?</p>
        <p>Instead, mix your mind and the Dharma together; that is the peak of the practice.</p>
      </div>
    </div>
    <div class="base-band"><div class="emblem" role="img" aria-label="Conch shell emblem"></div></div>
  </article>

  <article class="banner">
    <div class="illustration left" role="img" aria-label="Faint line drawing of a seated deity"></div>
    <div class="banner__content">
      <header class="banner__header"><div class="banner__title-zh">需避免的错误</div><div class="banner__title-en">Mistakes To Avoid</div></header>
      <div class="text-bo" style="margin-left:18px">ལམ་ལོག་ལ་གོམ་པ་མ་སྤོ་ཞིག།<br>སེམས་ཡིད་ལོག་པ་ལ་མ་གཏད་ཅིག།<br>སྐྱབས་ལོག་པ་ལ་མ་བཅོལ་ཅིག།<br>གྲོགས་ལོག་ལ་བསམ་པ་མ་བཤད་ཅིག།</div>
      <div class="text-zh wide" style="margin-left:40px">莫移迈步踏错路，<br>心交托人莫误，<br>所依皈依莫误依，<br>诚心告知友莫误。</div>
      <div class="text-en regular" style="margin-top:16px">
        Do not tread the wrong path.<br>Do not entrust your mind to the wrong person.<br>Do not seek refuge in the wrong guardian.<br>Do not confide your thoughts to the wrong friend.
      </div>
    </div>
    <div class="base-band"><div class="emblem" role="img" aria-label="Dharma wheel emblem"></div></div>
  </article>

  <article class="banner">
    <header class="banner__header"><div class="banner__title-zh">勿闲</div><div class="banner__title-en">Don't Dally</div></header>
    <div class="text-bo" style="margin-left:18px">མ་གཡེང་མ་གཡེང་འཆི་བདག་མྱུར་དུ་འོང་།<br>འཆི་བ་གློ་བུར་བྱུང་ན་ཅི་བྱ་ཡོད།<br>མ་ལེ་མ་ལེ་ད་ལྟ་ཆོས་ལ་བརྩོན།<br>བར་དོར་ཆོས་མེད་སུ་ཡིས་སྐྱོབ་པར་བྱེད།</div>
    <div class="text-zh wide" style="margin-left:40px">莫散莫散死亡迅速临，<br>死亡突然来到当何为？<br>莫停莫停精进于正法，<br>无法流转中有谁救护？</div>
    <div class="text-en regular" style="margin-top:30px">
      <p>Don't be distracted, don't be distracted, for quickly death will come.</p>
      <p>What can you do when death suddenly comes?</p>
      <p>Don't dally, don't dally, exert yourself in the excellent Dharma.</p>
      <p>Without the Dharma, who can protect you when you wander in the bardo?</p>
    </div>
    <div class="base-band"><div class="emblem" role="img" aria-label="Fish emblem"></div></div>
  </article>

  <article class="banner">
    <header class="banner__header"><div class="banner__title-zh">过于污垢</div><div class="banner__title-en">Excessive Dirt</div></header>
    <div class="text-bo" style="margin-left:18px">ཕྲག་དོག་ཆེ་ན་སེམས་མི་སྐྱིད།<br>རང་འདོད་ཆེ་ན་གྲོགས་མི་འོང་།<br>རེ་བ་ཆེ་ན་དོན་མི་འགྲུབ།<br>གཡོ་སྒྱུ་ཆེ་ན་ཡིད་མི་ཆེས།</div>
    <div class="text-zh wide" style="margin-left:40px">嫉妒若盛心不乐，<br>自利若盛友不来，<br>贪婪若盛目不成，<br>狡诈若多人不信。</div>
    <div class="text-en regular" style="margin-top:30px">
      <p>If your envy is great, your mind will not be joyful.</p>
      <p>If your self-centredness is great, you will not gain friends.</p>
      <p>If your greed is great, your goal will not be accomplished.</p>
      <p>If your deceitfulness is great, your credibility will be lost.</p>
    </div>
    <div class="base-band"><div class="emblem" role="img" aria-label="Twin wheels emblem"></div></div>
  </article>

  <article class="banner">
    <header class="banner__header"><div class="banner__title-zh">十大遗憾（上）</div><div class="banner__title-en">Ten Regrets (Part I)</div></header>
    <div class="two-col">
      <div class="text-bo" style="margin:0">དལ་འབྱོར་ཐོབ་ཀྱང་ཆོས་མ་བྱས།<br>ལུས་རྟེན་ཐོབ་ཀྱང་དོན་མ་གྲུབ།<br>ཚེ་ཐུང་དུས་ངན་སྡིག་ལ་བརྩོན།<br>རང་སེམས་ཆོས་སྐུ་མ་ཤེས་པར།<br>བླ་མ་དང་ནི་བྲལ་བར་གྱུར།</div>
      <div class="text-zh" style="margin:0;font-size:4.6px">暇满人身不修法，<br>可惜可叹真遗憾；<br>得此人身无所成，<br>空过此生真遗憾；<br>寿短时恶仍造罪，<br>此乃可悲真遗憾；<br>不识自心本法身，<br>沉溺轮回真遗憾；<br>未证菩提离上师，<br>孤身无依真遗憾。</div>
    </div>
    <div class="text-en regular" style="margin-top:14px">
      <p>It is regrettable to take joy in acts of non-virtue and evil when you have this unattained human body that is hard to obtain.</p>
      <p>It is regrettable to die as an ordinary person without the Dharma, when you have this fortunate human body with leisure, wealth and properties that is hard to obtain.</p>
      <p>It is regrettable to exhaust yourself in senseless and meaningless activities in this age of degeneration when your human lifespan is short and will pass in an instant.</p>
      <p>It is regrettable to be sunk in the mire of samsaric confusion when your unelaborated natural mind is the nature of dharmakaya.</p>
      <p>It is regrettable to be separated from your holy guru, the guide on the path, before you attain enlightenment.</p>
    </div>
    <div class="base-band"><div class="emblem" role="img" aria-label="Treasure vase emblem"></div></div>
  </article>

  <article class="banner">
    <header class="banner__header"><div class="banner__title-zh">十大遗憾（下）</div><div class="banner__title-en">Ten Regrets (Part II)</div></header>
    <div class="two-col">
      <div class="text-bo" style="margin:0">གསུམ་ཚོགས་ལུས་ངག་ཡིད་གསུམ།<br>དགེ་བ་ལ་མ་སྤྱད་པར།<br>ཐ་མལ་དུ་བཞག་པ་ནི།<br>འགྱོད་པའི་གནས་ཡིན་ནོ།</div>
      <div class="text-zh" style="margin:0;font-size:4.6px">三门身语意清净，<br>本应修持善妙法，<br>却于平庸中虚度，<br>散漫度日真遗憾；<br>蕴聚五蕴所成身，<br>未用修行真遗憾。</div>
    </div>
    <div class="text-en regular" style="margin-top:14px">
      <p>It is regrettable when the three doors of young adults in their prime stay in the ordinary state of indifference (to practising the Dharma).</p>
    </div>
    <div class="notes" style="margin-left:20px;font-size:3.8px">1. aggregates: the five heaps of form, feeling, perception, formation and consciousness.<br>2. three doors: body, speech and mind.</div>
    <div class="text-zh" style="margin:40px 0 2px 20px;font-size:4.6px">愿众佛陀汇聚加持。</div>
    <div class="text-en regular" style="margin-left:20px;font-size:3.8px">May all the Buddhas gather together.</div>
    <div class="base-band"><div class="emblem" role="img" aria-label="Sacred syllable emblem"></div></div>
  </article>

</main>
</body>
</html>
```